Brightmoor Glowing - Two Pages of Information and Pictures

We need a two page summary of the Service Offerings of Brightmoor Glowing - a company that installs LED Lighting. We've written the copy and picked images and chart that we like and have laid it out a word document.

We're looking for someone to design a more professional page layout than the generic Word Template. Please do not feel the current layout is suggested. It is only laid out this way because Word had that template. Be as creative as you want.

We would like the images and text to be in the same order that it is in now.

We're also in a rush so speed is appreciated. THANK YOU !!

Target Market(s)

Corporate Offices in New York

Industry/Entity Type

Lighting Fixture

Colors
85cae6
87cfc7
9bcb3c
3377b5

Requirements
Must have
• Must include two pages of the copy and images written and provided in the word document that was uploaded. Must use the Brightmoor colors in the logo.
Nice to have
• An easy to read flow of images and.

```html
<!DOCTYPE html>
<html lang="en">
<head>
<meta charset="utf-8">
<title>Brightmoor Glowing – Two Page Summary</title>
<link href="https://fonts.googleapis.com/css2?family=Bebas+Neue&family=Montserrat:wght@400;500;700&display=swap" rel="stylesheet">
<style>
  :root{
    --stage:#e6e6e6;
    --paper:#f4f4f4;
    --paper-edge:#ffffff;
    --green:#5f8d5f;
    --green-dark:#4f7b51;
    --green-soft:#86b46f;
    --blue:#6f9fb4;
    --blue-soft:#8fb8cb;
    --headline-blue:#5a8ba5;
    --ink:#333;
    --muted:#555;
    --rule:#bdbdbd;
  }
  *{margin:0;padding:0;box-sizing:border-box}
  html,body{width:1200px;height:817px;overflow:hidden;background:var(--stage);font-family:"Montserrat",Arial,sans-serif;color:var(--ink)}
  .page{position:absolute;top:68px;width:483px;height:676px;background:linear-gradient(180deg,var(--paper-edge) 0%,var(--paper) 60%,#ececec 100%);box-shadow:0 2px 6px rgba(0,0,0,.18);overflow:hidden}
  .page--front{left:94px}
  .page--back{left:615px}
  .abs{position:absolute}

  /* front */
  .hero{position:absolute;left:0;top:0}
  .brand-name{position:absolute;left:0;width:100%;text-align:center;font-weight:500;color:var(--green-dark);letter-spacing:1px}
  .brand-name--front{top:268px;font-size:19px}
  .tagline{position:absolute;top:339px;width:100%;text-align:center;font-size:11px;color:#444}
  .marker{position:absolute;top:370px;left:236px;width:0;height:0;border-left:5px solid transparent;border-right:5px solid transparent;border-top:7px solid var(--green-dark)}
  .headline{position:absolute;width:100%;text-align:center;font-family:"Bebas Neue",Impact,sans-serif;line-height:1;letter-spacing:.5px}
  .headline--cost{top:395px;font-size:56px;color:var(--headline-blue)}
  .headline--turnkey{top:448px;font-size:56px;color:var(--green)}
  .intro{position:absolute;top:524px;left:53px;width:380px;font-size:9.6px;line-height:12.1px;text-align:justify;text-align-last:center;color:#333}

  /* contact strip */
  .contact-tab{position:absolute;top:626px;left:186px;width:110px;height:20px;background:var(--blue);clip-path:polygon(12% 0,88% 0,100% 100%,0 100%);color:#fff;font-weight:500;font-size:9.5px;text-align:center;line-height:21px;letter-spacing:.4px}
  .contact-bar{position:absolute;top:646px;left:0;width:100%;height:18px;background:var(--green);display:flex;align-items:center;justify-content:center;gap:14px;color:#fff;font-size:7.6px;font-weight:500;letter-spacing:.2px}
  .contact-item{display:flex;align-items:center;gap:5px}
  .contact-item svg{width:9px;height:9px}

  /* back */
  .header-band{position:absolute;left:0;top:0}
  .brand-name--back{top:20px;font-size:10px;color:#fff;letter-spacing:2px}
  .section-title{position:absolute;left:12px;font-weight:700;font-size:10.5px;color:var(--green-dark);letter-spacing:.2px}
  .section-title::before{content:"";position:absolute;left:-12px;top:1px;width:5px;height:10px;background:var(--blue)}
  .copy{position:absolute;font-size:7.3px;line-height:10.2px;text-align:justify;color:#333}
  .chart{position:absolute;left:253px;top:110px;width:218px;height:136px;background:#fff;border:1px solid #ddd}
  .team-photo{position:absolute;left:257px;top:296px;width:214px;height:124px;background:linear-gradient(160deg,#6c8a55 0%,#5d7c9c 45%,#7d9fbf 70%,#4e6b3e 100%);box-shadow:0 2px 4px rgba(0,0,0,.25)}
  .quote{position:absolute;left:12px;width:459px;border:1px solid var(--rule);text-align:center;font-size:7.6px;line-height:10.4px;color:#333;padding:6px 12px 0}
  .quote cite{display:block;font-style:normal;font-weight:700;color:var(--green-dark);font-size:7.8px}
</style>
</head>
<body>

<!-- FRONT -->
<section class="page page--front">
  <svg class="hero" width="483" height="340" viewBox="0 0 483 340">
    <polygon points="0,0 102,0 0,104" fill="#8fb6ca"/>
    <polygon points="386,0 483,0 483,104" fill="#8fb6ca"/>
    <polygon points="0,236 82,328 0,328" fill="#5f8d5f"/>
    <polygon points="483,236 401,328 483,328" fill="#5f8d5f"/>
    <polygon points="0,270 52,328 0,328" fill="#86b46f"/>
    <polygon points="483,270 431,328 483,328" fill="#86b46f"/>
    <defs>
      <linearGradient id="office" x1="0" y1="0" x2="1" y2="1">
        <stop offset="0" stop-color="#e8e6e0"/><stop offset=".55" stop-color="#9a9892"/><stop offset="1" stop-color="#5a5752"/>
      </linearGradient>
      <linearGradient id="lobby" x1="0" y1="0" x2="0" y2="1">
        <stop offset="0" stop-color="#3b332c"/><stop offset=".5" stop-color="#9b7a56"/><stop offset="1" stop-color="#cbb89b"/>
      </linearGradient>
      <radialGradient id="bulbs" cx=".55" cy=".55" r=".6">
        <stop offset="0" stop-color="#f0c27a"/><stop offset=".5" stop-color="#8a5a2e"/><stop offset="1" stop-color="#3a2718"/>
      </radialGradient>
    </defs>
    <g role="img" aria-label="Photo of an open-plan office lit by LED fixtures">
      <polygon points="118,44 234,180 118,316 0,178 0,180" fill="url(#office)"/>
    </g>
    <g role="img" aria-label="Photo of a lobby with a row of track lights over wood panels">
      <polygon points="104,0 382,0 243,166" fill="url(#lobby)"/>
    </g>
    <g role="img" aria-label="Photo of hanging filament-style LED bulbs">
      <polygon points="368,44 490,180 368,316 252,180" fill="url(#bulbs)"/>
    </g>
  </svg>
  <div class="brand-name brand-name--front">BRIGHTMOOR</div>
  <p class="tagline">Making LEDs beautiful.</p>
  <div class="marker"></div>
  <h1 class="headline headline--cost">No Upfront Cost</h1>
  <h2 class="headline headline--turnkey">Turnkey LEDs</h2>
  <p class="intro">Brightmoor Glowing provides LED lighting as a service – fully implemented and managed LEDs at no upfront cost. Brightmoor takes the risk, hassle and capital cost out of adopting LED’s energy saving technology. Brightmoor guarantees net-savings for customers on day one, and continues to guarantee savings and performance for the full term of the contract. And the savings add up! A project can be installed 2-4 weeks from kickoff, and projects continue to generate savings for up to 10 years.</p>

  <div class="contact-tab">CONTACT US</div>
  <div class="contact-bar">
    <span class="contact-item"><svg viewBox="0 0 10 10"><rect x="0.5" y="2" width="9" height="6" fill="none" stroke="#fff"/><path d="M0.5 2 L5 5.5 L9.5 2" fill="none" stroke="#fff"/></svg>CUSTOMERS@BRIGHTMOORGLOWING.COM</span>
    <span class="contact-item"><svg viewBox="0 0 10 10"><path d="M2 1 L4 3 L3 4.5 Q4.5 6.5 5.5 7 L7 6 L9 8 L7.5 9.5 Q3 8.5 0.5 2.5 Z" fill="#fff"/></svg>347 555 GLOW</span>
    <span class="contact-item"><svg viewBox="0 0 10 10"><circle cx="5" cy="5" r="4.3" fill="none" stroke="#fff"/><ellipse cx="5" cy="5" rx="2" ry="4.3" fill="none" stroke="#fff"/><path d="M0.7 5 H9.3" stroke="#fff"/></svg>BRIGHTMOORGLOWING.COM</span>
  </div>
</section>

<!-- BACK -->
<section class="page page--back">
  <svg class="header-band" width="483" height="100" viewBox="0 0 483 100">
    <polygon points="0,0 483,0 483,88 241,46 0,88" fill="var(--green)"/>
    <polyline points="0,92 241,50 483,92" fill="none" stroke="#d9d9d9" stroke-width="2"/>
  </svg>
  <div class="brand-name brand-name--back">BRIGHTMOOR</div>

  <h3 class="section-title" style="top:107px">WHY USE BRIGHTMOOR?</h3>
  <p class="copy" style="left:12px;top:122px;width:226px">Brightmoor’s customers understand the value of LEDs but don’t want to deal with the risk, hassle and capital cost on their own. Brightmoor starts saving customers money the first month – typically a net-savings of about 4.7 cents a square-foot per month. Brightmoor will design aesthetic LED systems and install the best available technology.</p>
  <p class="copy" style="left:12px;top:194px;width:226px">Brightmoor provides LEDs at the best cost with its as-a-service structure, which puts the cost of lighting into clients’ monthly operating budget for less than they save. By installing projects immediately, Brightmoor eliminates the cost of foregone savings that would accumulate from delayed implementation.</p>

  <div class="chart">
    <svg width="218" height="136" viewBox="0 0 218 136" role="img" aria-label="Bar and line chart of annual and total net-savings over ten years">
      <text x="109" y="11" text-anchor="middle" font-family="Montserrat,Arial,sans-serif" font-size="6.8" fill="#333">Annual and Total Net-Savings of 250,000 ft2 Customer</text>
      <g font-family="Montserrat,Arial,sans-serif" font-size="3.6" fill="#666">
        <text x="16" y="22">$300</text><text x="16" y="42">$250</text><text x="16" y="62">$200</text><text x="16" y="82">$150</text><text x="16" y="101">$100</text><text x="18" y="120">$50</text><text x="20" y="139">$-</text>
        <text x="196" y="22">$2.0</text><text x="196" y="42">$1.6</text><text x="196" y="62">$1.2</text><text x="196" y="82">$0.8</text><text x="196" y="101">$0.4</text><text x="196" y="120">$0.0</text>
      </g>
      <line x1="30" y1="120" x2="192" y2="120" stroke="#ccc" stroke-width=".5"/>
      <g fill="#9cc9c9">
        <rect x="36" y="99" width="4" height="21"/><rect x="52" y="99" width="4" height="21"/><rect x="68" y="99" width="4" height="21"/><rect x="84" y="99" width="4" height="21"/><rect x="100" y="99" width="4" height="21"/>
      </g>
      <g fill="#6fa962">
        <rect x="41" y="84" width="5" height="36"/><rect x="57" y="84" width="5" height="36"/><rect x="73" y="84" width="5" height="36"/><rect x="89" y="84" width="5" height="36"/><rect x="105" y="84" width="5" height="36"/>
        <rect x="121" y="45" width="5" height="75"/><rect x="137" y="45" width="5" height="75"/><rect x="153" y="45" width="5" height="75"/><rect x="169" y="45" width="5" height="75"/><rect x="185" y="45" width="5" height="75"/>
      </g>
      <polyline points="40,120 56,112 72,104 88,96 104,89 120,76 136,63 152,50 168,37 184,24" fill="none" stroke="#777" stroke-width=".7"/>
      <g font-family="Montserrat,Arial,sans-serif" font-size="3.4" fill="#666">
        <text x="40" y="127">1</text><text x="56" y="127">2</text><text x="72" y="127">3</text><text x="88" y="127">4</text><text x="104" y="127">5</text><text x="120" y="127">6</text><text x="136" y="127">7</text><text x="152" y="127">8</text><text x="168" y="127">9</text><text x="183" y="127">10</text>
        <rect x="42" y="131" width="6" height="2" fill="#9cc9c9"/><text x="50" y="133">Annual Service Cost</text>
        <rect x="96" y="131" width="6" height="2" fill="#6fa962"/><text x="104" y="133">Annual Net-Savings</text>
        <line x1="146" y1="132" x2="152" y2="132" stroke="#777" stroke-width=".6"/><text x="154" y="133">Total Net-Savings</text>
      </g>
    </svg>
  </div>

  <p class="copy" style="left:12px;top:253px;width:459px">It can be risky to adopt new technology, especially when salespeople try to sell more than is needed. Brightmoor has access to better equipment and at better cost than is widely available on the open market and passes that quality and savings on to its customers. Brightmoor guarantees performance for 5 years, which removes the risk of a failed project.</p>

  <h3 class="section-title" style="top:293px">THE BEST TEAM IN LEDS</h3>
  <p class="copy" style="left:12px;top:307px;width:235px">Brightmoor is a team of lighting experts who get the evolution of lighting and efficiency. Simply put, we come in up every day with one goal: to provide an excellent service that saves money and uses less electricity. Part of the team focuses on the supply chain of the very best equipment that customers have come to appreciate. Part of the team focuses on the project management of each installation. And, part of the team focuses on resolving any questions customers might have in their transition. Together we make up the best team in LEDs and work tirelessly to make it easy to upgrade.</p>
  <div class="team-photo" role="img" aria-label="Photo of team members in matching blue shirts, seen from behind in a garden"></div>

  <h3 class="section-title" style="top:426px">TESTIMONIALS</h3>
  <blockquote class="quote" style="top:450px;height:44px">“ Brightmoor made a huge improvement in the lighting for our headquarters.<br>The installation process was as smooth as can be and the service since has been excellent.”<cite>NORTHPOINT HEALTH</cite></blockquote>
  <blockquote class="quote" style="top:506px;height:44px">“ In a museum, quality lighting is paramount. Brightmoor has been a great partner in helping us transition to LEDs that look great, save us money, and make lighting management so much simpler. ”<cite>HARBORVIEW MUSEUM OF ART, NEW YORK</cite></blockquote>
  <blockquote class="quote" style="top:561px;height:50px">“ We are so happy to have had Brightmoor’s help building out our new office space – they put their lighting expertise to work delivering beautiful LEDs and fixtures. It was cost-effective, removed lighting from the build-out budget, and it’s been a joy to work with them since.”<cite>FIELDSTONE WORKS, INC</cite></blockquote>

  <div class="contact-tab">CONTACT US</div>
  <div class="contact-bar">
    <span class="contact-item"><svg viewBox="0 0 10 10"><rect x="0.5" y="2" width="9" height="6" fill="none" stroke="#fff"/><path d="M0.5 2 L5 5.5 L9.5 2" fill="none" stroke="#fff"/></svg>CUSTOMERS@BRIGHTMOORGLOWING.COM</span>
    <span class="contact-item"><svg viewBox="0 0 10 10"><path d="M2 1 L4 3 L3 4.5 Q4.5 6.5 5.5 7 L7 6 L9 8 L7.5 9.5 Q3 8.5 0.5 2.5 Z" fill="#fff"/></svg>347 555 GLOW</span>
    <span class="contact-item"><svg viewBox="0 0 10 10"><circle cx="5" cy="5" r="4.3" fill="none" stroke="#fff"/><ellipse cx="5" cy="5" rx="2" ry="4.3" fill="none" stroke="#fff"/><path d="M0.7 5 H9.3" stroke="#fff"/></svg>BRIGHTMOORGLOWING.COM</span>
  </div>
</section>

</body>
</html>
```